A4 Certificate design, as a gift to put on the wall

This is a product that will need to look like someone wants this on their wall, the website will also be led by the style and colours of the certificate.

A certificate that is to include date, time, photo (although not all will have photos, so maybe a generic bit of art), and short message, the look is to be generic, arty, not to busy, warm with an official look, that is to look nice on a wall, some art work and ideas included.
I need a certificate designing that is to celebrate somebodies memory, basically the concept is a certificate that has a date and time that is changeable, to be included year, month, day, hour, minute (Written or as numbers) a photo that could potentially be of anything so this will reflect how the certificate boarder/background etc is going to look as it could be wedding, anniversary, birth, holiday, concert …….etc, also included is a text box where the person will dedicate or write a short piece about this memory and a from and to field. Please see attached.
The certificate is to include the company logo as attached Catch a Lantern, and the stamp in the bottom right of the Bramwell Seal Bureau, a couple of versions are available, attached is also some text and a couple of photos to use as an idea, or create your own, a very rough example is included, I am not a designer! Lol
The size of the certificate is A4 either landscape or preferably portrait, all the text is to be of your choice, style, colour, Logo is also possibly changeable for colour preferences
Colours to include should be pastels and soft, this is a certificate people are going to want to put up on their wall, so should not look like a crazy arty poster as this is to appeal to a wide market of people, ages from 8-80 and sex.
Open to lots of ideas so lets see some creative flair, if I like your style then in the near future there will be scope to make more dedicated similar certificates, to give people more choices.

Any questions please feel free to email me

Target Market(s)

Wide range of people as possible from teenage up to elders 8-80

Industry/Entity Type

Gift Shop

Other font styles liked:
• Arty is fine as long as readable

Requirements
Must have
• Must include catch a lantern logo, BSB round stamp(must be stamp size apx 30mm Diameter), year, time and date to be clear and visible, lend a paw logo to be smaller and a bit tucked away as this is a charity we sponsor.
• Pastels colours nothing too bright
• Appeal to all ages and sex`s
• Easily readable text message but slightly arty,
• Must include names from and to.
• Photo not to be any bigger than 130mm length x 80mm height,
Nice to have
• Background art, simple border art, generic for old ages and sex`s
Should not have
• Do not want cheesy just won a race certificate look
• No dark colours

```html
<!DOCTYPE html>
<html lang="en">
<head>
<meta charset="utf-8">
<title>Catch a Lantern – Moment Certificate</title>
<link rel="stylesheet" href="https://fonts.googleapis.com/css2?family=Cinzel:wght@700&family=Comic+Neue:wght@700&family=Montserrat:wght@600&display=swap">
<style>
  :root {
    --paper: #ffffff;
    --ink: #111111;
    --ring-grey: #a9a9a9;
    --seal-red: #e2383f;
    --brand-grey: #3d3d3d;
  }
  html, body {
    margin: 0;
    padding: 0;
    width: 849px;
    height: 1200px;
    overflow: hidden;
    background: var(--paper);
  }
  .certificate {
    position: relative;
    width: 849px;
    height: 1200px;
    overflow: hidden;
    background: var(--paper);
  }
  .artwork {
    position: absolute;
    inset: 0;
  }
  .registry-mark {
    position: absolute;
    left: 18px;
    top: 34px;
    display: flex;
    align-items: center;
    gap: 8px;
    font-family: "Montserrat", sans-serif;
    font-weight: 600;
    color: var(--seal-red);
  }
  .registry-mark__name {
    font-size: 28px;
    letter-spacing: 1px;
  }
  .registry-mark__full {
    font-size: 8px;
    line-height: 1.15;
    width: 62px;
  }
  .moment-date,
  .moment-time {
    position: absolute;
    margin: 0;
    text-align: center;
    font-family: "Cinzel", serif;
    font-weight: 700;
    line-height: 1;
  }
  .moment-date {
    color: var(--paper);
  }
  .moment-date--year {
    top: 160px;
    left: 157px;
    width: 534px;
    font-size: 94px;
  }
  .moment-date--day {
    top: 248px;
    left: 190px;
    width: 472px;
    font-size: 70px;
    letter-spacing: 1px;
  }
  .moment-time {
    top: 325px;
    left: 157px;
    width: 534px;
    font-size: 46px;
    color: var(--ink);
  }
  .dedication {
    position: absolute;
    left: 74px;
    top: 533px;
    width: 460px;
    font-family: "Comic Neue", cursive;
    font-weight: 700;
    font-size: 30px;
    line-height: 39px;
    color: var(--ink);
  }
  .dedication p {
    margin: 0 0 39px;
  }
  .brand {
    position: absolute;
    left: 28px;
    top: 1108px;
    margin: 0;
    font-family: "Montserrat", sans-serif;
    font-weight: 600;
    font-size: 31px;
    letter-spacing: 1px;
    line-height: 1;
    color: var(--brand-grey);
    text-transform: uppercase;
  }
</style>
</head>
<body>
<main class="certificate">
  <svg class="artwork" width="849" height="1200" viewBox="0 0 849 1200">
    <defs>
      <linearGradient id="facetWash" x1="0" y1="0" x2="1" y2="1">
        <stop offset="0" stop-color="#7a6aa6"/>
        <stop offset="0.35" stop-color="#c58bbb"/>
        <stop offset="0.65" stop-color="#9cc3d6"/>
        <stop offset="1" stop-color="#d987b0"/>
      </linearGradient>
      <linearGradient id="photoWash" x1="0" y1="0" x2="1" y2="1">
        <stop offset="0" stop-color="#dfe4e2"/>
        <stop offset="0.5" stop-color="#e9cdb4"/>
        <stop offset="1" stop-color="#c9b6a3"/>
      </linearGradient>
      <clipPath id="photoClip">
        <circle cx="672" cy="983" r="207"/>
      </clipPath>
    </defs>

    <polygon class="facet-field" role="img" aria-label="Soft low-poly pastel triangle artwork in violet, pink and sky blue"
      points="0,0 849,0 849,600 720,500 600,540 480,440 330,480 210,420 110,520 40,470 0,500"
      fill="url(#facetWash)" opacity="0.75"/>

    <line x1="157" y1="164" x2="691" y2="164" stroke="#ffffff" stroke-width="3"/>
    <line x1="192" y1="318" x2="691" y2="318" stroke="#ffffff" stroke-width="3"/>

    <path class="sweep-arc" d="M0,440 A560,560 0 0 1 584,712" fill="none" stroke="var(--ring-grey)" stroke-width="10"/>
    <path class="photo-ring" d="M444,983 A228,228 0 0 1 900,983" fill="none" stroke="var(--ring-grey)" stroke-width="10"/>

    <rect class="photo" role="img" aria-label="Photo of the celebrated moment: two friends smiling together outdoors"
      x="465" y="776" width="414" height="414" fill="url(#photoWash)" clip-path="url(#photoClip)"/>

    <circle class="seal" cx="769" cy="1133" r="58" fill="var(--seal-red)"/>
  </svg>

  <div class="registry-mark">
    <span class="registry-mark__name">BSB</span>
    <span class="registry-mark__full">Bramwell Seal Bureau</span>
  </div>

  <p class="moment-date moment-date--year">2016</p>
  <p class="moment-date moment-date--day">MARCH 24</p>
  <p class="moment-time">12:31</p>

  <section class="dedication">
    <p>To Tess</p>
    <p>I wish this moment when<br>we rocked out would last<br>forever, best friends and<br>best concert EVER!!</p>
    <p>From Lola</p>
  </section>

  <p class="brand">Catch a Lantern</p>
</main>
</body>
</html>
```